Creative, Modern and Conversion based Web Design

Kolvex Digital has recently launched a new logo and as part of our companies rebranding, we need a new website aimed towards the UK B2B marketplace.

The website needs to deliver a modern and creative website design whilst ensuring the design is tailored towards conversion optimisation.

This site must drive point of contact either from an online form, via a direct telephone call or Skype connection.

Our sales are all offline so the website will be a simple, elegant and stunning information portal.

Kolvex Digital offers Digital Marketing services to companies throughout the UK - our target audiences are companies that turnover a minimum of 3 million pounds a year and as such we need to deliver a professional image that installs confidence in our companies abilities.

We do not like websites that are reliant upon stock photography - we are happy for stock photography to be used in a small way however the site must not look like a template filled with stock photography.

What do we do

We supply digital marketing services to those companies who demand a strong return on investment - our company prides itself on delivering successful campaigns that help establish long-term profitable relationships.

A lot of the information presented on our old site is relevant today however the design sucks. So please use the information on our current website as a foundation for your design content.

I am looking for several page designs including

"Home Page" Desktop Version
"Service Page" Desktop Version
"Blog Page" Desktop Version

"Home Page" Mobile Version
"Service Page" Mobile Version
"Blog Page" Mobile Version

In the 1st instance please only submit a single design for the "Home Page" Desktop Version - those designers that we are impressed with will be asked to complete the other designs before a winner is selected.

I like modern clean fonts - the site needs to welcome the reader and encourage them to absorb the information - not to overload and make them leave.

The site must be designed to naturally fit our companies new logo.

NO TEMPLATES

Target Market(s)

B2b - 3 million turnover and above

Industry/Entity Type

Digital Marketing

Number of Pages Required

3 page

Requirements
Must have
• Blended well with the companies logo
• We need conversion optimisation to be a huge part of the design - we considered a conversation when a potential customer reaches out to use via - web form, telephone or skype
• The current content on the old website fits today's business but the design sucks.
• www.kolvexdigital-example.com
Nice to have
• We need 3 pages (in 2 variants Desktop and Mobile)
• Home Page
• Service Page
• Blog Page
• Please only deliver the "Home Page" desktop version - if we are happy with your design we will aks for the additional pages
Should not have
• No templates and not stock photo heavy design

```html
<!DOCTYPE html>
<html lang="en">
<head>
<meta charset="utf-8">
<title>Kolvex Digital – Search Marketing</title>
<link rel="stylesheet" href="https://fonts.googleapis.com/css2?family=Montserrat:wght@300;400;500;600&display=swap">
<style>
:root{
  --ink:#1d1d2b;
  --text:#6b6b7d;
  --purple:#8a6cf0;
  --violet-a:#c08af2;
  --violet-b:#6b5ae9;
  --pale:#f3f4fb;
  --line:#e7e7f2;
  --white:#ffffff;
}
*{box-sizing:border-box;margin:0;padding:0}
html,body{width:800px;height:1200px;overflow:hidden;background:var(--white)}
body{font-family:"Montserrat",sans-serif;color:var(--ink);position:relative}
.abs{position:absolute}
.site-header{position:absolute;left:0;top:0;width:800px;height:40px;z-index:5}
.brand{left:108px;top:8px;display:flex;align-items:center;gap:6px;font-size:11px;font-weight:600;color:var(--ink)}
.brand-mark{width:11px;height:11px;background:var(--ink)}
.nav{right:107px;top:8px;display:flex;align-items:center;gap:16px;font-size:8.5px;font-weight:500;color:var(--ink)}
.nav .contact{padding:5px 12px;border-radius:12px;background:var(--white);box-shadow:0 3px 10px rgba(90,80,180,.18)}
.hero-blob{left:330px;top:-40px;width:520px;height:260px;border-radius:50%;background:var(--pale)}
.hero-art{left:370px;top:52px;width:400px;height:134px;border-radius:14px;background:linear-gradient(120deg,#dfe3fb,#b8b0f3 55%,#f4c1c9)}
.hero-title{left:108px;top:90px;font-size:21px;font-weight:600}
.hero-sub{left:108px;top:114px;font-size:15px;font-weight:400}
.hero-text{left:108px;top:138px;width:240px;font-size:8px;line-height:11px;color:var(--text)}
.btn{display:inline-block;border-radius:14px;font-weight:500;text-align:center}
.btn-fill{background:linear-gradient(90deg,var(--violet-a),var(--violet-b));color:var(--white);box-shadow:0 4px 10px rgba(120,100,230,.35)}
.hero-btn{left:108px;top:165px;font-size:8px;padding:6px 16px}
.section-blob{left:0;top:300px;width:330px;height:130px;background:var(--pale);clip-path:polygon(0 0,100% 40%,100% 100%,0 100%)}
.lead{left:0;width:800px;top:250px;text-align:center;font-size:15px;line-height:21px;font-weight:400}
.badge{left:108px;top:305px;width:187px;height:114px;background:var(--white);border-radius:6px;box-shadow:0 10px 24px rgba(120,110,200,.22)}
.badge .stripe{left:0;top:28px;width:8px;height:44px;background:#4a78cf}
.badge .plate{left:24px;top:28px;width:120px;height:44px;background:#eef0f6;border-radius:4px}
.badge .dot{top:84px;width:60px;height:16px;background:#eef0f6;border-radius:4px}
.about{left:359px;top:312px;width:334px;font-size:7.6px;line-height:12px;color:var(--text)}
.about strong{display:block;margin-top:8px;color:var(--ink);font-weight:500}
.card{width:175px;height:100px;background:var(--white);border-radius:6px 6px 22px 6px;box-shadow:0 8px 22px rgba(120,110,200,.16);text-align:center;padding:9px 12px}
.card h3{font-size:9px;font-weight:600;margin-bottom:5px}
.card p{font-size:7px;line-height:9.3px;color:var(--text)}
.card .pill{position:absolute;left:50%;bottom:9px;transform:translateX(-50%);font-size:7px;padding:3px 12px;white-space:nowrap}
.card.featured{background:linear-gradient(160deg,var(--violet-a),var(--violet-b))}
.card.featured h3,.card.featured p{color:var(--white)}
.card.featured .pill{background:var(--white);color:var(--ink)}
.stats{left:0;top:719px;width:800px;height:76px;background:linear-gradient(90deg,#b18af0,#8f78ee 50%,#a98bf3);color:var(--white)}
.stats .tag{top:11px;width:800px;text-align:center;font-size:13px;font-weight:300}
.stat{top:34px;width:200px;text-align:center}
.stat b{display:block;font-size:17px;font-weight:600}
.stat span{font-size:10.5px;font-weight:300}
.seo-blob{left:0;top:800px;width:300px;height:230px;background:var(--pale);clip-path:polygon(0 0,100% 0,60% 100%,0 100%)}
.seo-title{left:0;width:800px;top:830px;text-align:center;font-size:13px;font-weight:500}
.seo-sub{left:0;width:800px;top:849px;text-align:center;font-size:9.5px}
.seo-text{left:108px;top:866px;width:585px;font-size:7px;line-height:9.5px;color:var(--text)}
.seo-text h4{font-size:7.3px;font-weight:600;color:var(--ink);margin:5px 0 3px}
.seo-text li{list-style:none;position:relative;padding-left:13px;margin-bottom:2px}
.seo-text li svg{position:absolute;left:0;top:1px}
.seo-link{left:0;width:800px;top:978px;text-align:center;font-size:7.5px;color:var(--ink)}
.seo-link a{color:var(--purple);text-decoration:none;font-weight:500}
.partners{left:108px;top:1008px;width:585px;display:flex;justify-content:space-between;align-items:center;font-size:11px;font-weight:600;color:#7b7b88}
.partners span{display:flex;align-items:center;gap:4px}
.partners i{display:inline-block;width:9px;height:9px;background:#9a9aa6}
.cta{left:108px;top:1055px;width:585px;height:76px;border-radius:4px 4px 40px 4px;background:linear-gradient(100deg,#c690f2,#8c72ee 55%,#6c5ae8);color:var(--white);text-align:center;padding-top:14px}
.cta h2{font-size:13px;font-weight:500}
.cta p{font-size:7.5px;font-weight:300;margin-top:5px}
.cta .pill{background:var(--white);color:var(--ink);font-size:7px;padding:4px 10px;margin-top:9px}
.footer{left:108px;top:1176px;width:585px;display:flex;align-items:center;font-size:7.5px}
.footer .brand-sm{display:flex;align-items:center;gap:5px;font-weight:600;font-size:9px}
.footer .copy{color:#c5c5d0;margin-left:20px}
.footer nav{margin-left:auto;display:flex;gap:14px;font-weight:500}
</style>
</head>
<body>
<div class="abs hero-blob"></div>
<div class="abs hero-art" role="img" aria-label="Illustration of two people presenting growth charts on a large screen beside a chair and plant"></div>

<header class="site-header">
  <div class="abs brand"><span class="brand-mark"></span>Kolvex Digital</div>
  <nav class="abs nav"><span>Home</span><span>Services ▾</span><span>White Label Link Building</span><span class="contact">Contact Us</span></nav>
</header>

<h1 class="abs hero-title">Search Marketing</h1>
<p class="abs hero-sub">that actually delivers</p>
<p class="abs hero-text">Search marketing is our forte. Our client results highlight just how good we do it.</p>
<a class="abs btn btn-fill hero-btn">Learn more</a>

<div class="abs section-blob"></div>
<h2 class="abs lead">Do you want to see an enviable ROI on search marketing?<br>It’s possible – you’ve found us.</h2>

<div class="abs badge" role="img" aria-label="Certified partner badge">
  <div class="abs stripe"></div><div class="abs plate"></div>
  <div class="abs dot" style="left:14px"></div><div class="abs dot" style="left:100px"></div>
</div>
<div class="abs about">
  We know and understand the world of business. We know that ROI is the single most important metric in the marketing world. We’ve worked within some of the world’s largest industries – such as finance, insurance, payday loans and health, where achieving above 100% ROI is often impossible. For us, it’s just a challenge that can be overcome. Whether we’re working with you to drive your Pay-Per-Click Marketing, Organic Search Marketing (SEO), Email Marketing or Lead Filtering &amp; Delivery – we always have your ROI in mind. That’s why we’re known as the ROI driven digital agency.
  <strong>Handle your SEO in-house? Consider using our industry-leading link outreach service to bolster your efforts.</strong>
</div>

<section>
  <div class="abs card" style="left:108px;top:462px"><h3>Organic Search</h3><p>Attract traffic that converts and interacts with your brand through Organic. We implement both short-term and long-term campaigns to bolster your success.</p><span class="btn btn-fill pill">Organic Search</span></div>
  <div class="abs card featured" style="left:312px;top:462px"><h3>Email Marketing</h3><p>Drive highly converting traffic to your website. Our PPC campaigns are ROI-driven from the start – helping you to scale your business quickly.</p><span class="btn pill">Paid Search</span></div>
  <div class="abs card" style="left:517px;top:462px"><h3>Link Outreach</h3><p>The core foundation of any search campaign. Our team of link outreachers are the best in the industry. We secure link placements that drive rankings.</p><span class="btn btn-fill pill">Link Outreach</span></div>
  <div class="abs card" style="left:108px;top:578px"><h3>UX &amp; CRO</h3><p>Let us dig into your analytic channels and identify where we can bolster your conversion rates while improving user experience.</p><span class="btn btn-fill pill">UX &amp; CRO</span></div>
  <div class="abs card" style="left:312px;top:578px"><h3>Email Marketing</h3><p>Our targeted email marketing campaigns allow you to segment users and deliver custom-tailored campaigns and promotions to different demographics.</p><span class="btn btn-fill pill">Email Marketing</span></div>
  <div class="abs card" style="left:517px;top:578px"><h3>Social Media</h3><p>Your followers are your most loyal customers. Let us develop a comprehensive strategy that aligns your brand with interests, while driving increased sales.</p><span class="btn btn-fill pill">Social Media</span></div>
</section>

<section class="abs stats">
  <p class="abs tag">We grow as our clients grow. That’s what we love.</p>
  <div class="abs stat" style="left:58px"><b>117</b><span>Satisfied Clients</span></div>
  <div class="abs stat" style="left:300px"><b>215</b><span>Campaigns Finished</span></div>
  <div class="abs stat" style="left:541px"><b>1,798</b><span>Cups of Coffee</span></div>
</section>

<div class="abs seo-blob"></div>
<h2 class="abs seo-title">Handle SEO Yourself? Perfect</h2>
<p class="abs seo-sub">Hassle-Free Link Placements That Drive Rankings</p>
<div class="abs seo-text">
  <p>Our link placements are used by some of the world’s largest companies in the most difficult industries – such as payday loans, insurance, finance, health and legal. We use our link placement service in conjunction with our Organic Search (SEO) offerings, although some of our clients handle their SEO in-house and prefer to use our link placements to bolster their rankings.</p>
  <h4>Here’s how our unique, link acquisition process works:</h4>
  <ul>
    <li><svg width="8" height="8" viewBox="0 0 8 8"><rect width="8" height="8" rx="1" fill="#6b5ae9"/><path d="M2 4l1.5 1.5L6 2.5" stroke="#fff" fill="none"/></svg>We take your clients URLs and their business sector (or your own sites), and we utilise our connections to try and secure a link placement.</li>
    <li><svg width="8" height="8" viewBox="0 0 8 8"><rect width="8" height="8" rx="1" fill="#6b5ae9"/><path d="M2 4l1.5 1.5L6 2.5" stroke="#fff" fill="none"/></svg>All of the sites we outreach too are 100% genuine – we do not own nor control any of the sites.</li>
    <li><svg width="8" height="8" viewBox="0 0 8 8"><rect width="8" height="8" rx="1" fill="#6b5ae9"/><path d="M2 4l1.5 1.5L6 2.5" stroke="#fff" fill="none"/></svg>If a webmaster chooses to link to you, it is of their own accord. They have decided to link to you. Thus, you have earned a genuine link.</li>
    <li><svg width="8" height="8" viewBox="0 0 8 8"><rect width="8" height="8" rx="1" fill="#6b5ae9"/><path d="M2 4l1.5 1.5L6 2.5" stroke="#fff" fill="none"/></svg>We will identify the most relevant page/post on their site, and work with the webmaster to weave your links into their existing content. We will write an additional sentence or two to make sure the anchor text fits in with the content.</li>
  </ul>
</div>
<p class="abs seo-link">Want to learn more and get our pricing? <a>Just click here →</a></p>

<div class="abs partners">
  <span><i></i>Metricsa</span><span>Rankwell</span><span>Probe</span><span>Heatly</span><span><i></i>Adplex</span><span>Seekr</span>
</div>

<section class="abs cta">
  <h2>Want To Improve Your ROI? Let’s Talk</h2>
  <p>We’ll never turn down an opportunity to discover how we can help grow your business.</p>
  <span class="btn pill">Email Marketing</span>
</section>

<footer class="abs footer">
  <div class="brand-sm"><span class="brand-mark"></span>Kolvex Digital</div>
  <span class="copy">© 2018 Kolvex Digital Limited</span>
  <nav><span>Services</span><span>White Label Link Building</span><span>Contact Us</span></nav>
</footer>
</body>
</html>
```